St Louis Electrician Needing a Business Card Design!!

We are a St Louis based electrical contracting firm that needs help designing a business card. We have a logo and I have another image that I would like to incorporate. Open to ideas..Thanks!!

Industry/Entity Type

Business

Requirements
Must have
• there are two downloads...one is the logo and the other is what i was wanting coming off the logo...the light rays. Like the logo with the blue background...Was thinking the whole card would be that color blue.
Should not have
• No lightning bolts

```html
<!DOCTYPE html>
<html lang="en">
<head>
<meta charset="utf-8">
<title>Voltaline Inc. — Business Card</title>
<link rel="stylesheet" href="https://fonts.googleapis.com/css2?family=Cinzel:wght@400;600&family=Marcellus&display=swap">
<style>
  :root {
    --page-bg: #e9e7e3;
    --card-blue: #1c5bb3;
    --card-blue-deep: #134b9c;
    --ink-white: #ffffff;
    --ink-soft: rgba(255, 255, 255, 0.92);
  }
  * { box-sizing: border-box; margin: 0; padding: 0; }
  html, body {
    width: 1200px;
    height: 950px;
    overflow: hidden;
    background: var(--page-bg);
  }
  .card {
    position: absolute;
    left: 75px;
    top: 175px;
    width: 1050px;
    height: 600px;
    background: linear-gradient(135deg, var(--card-blue) 0%, var(--card-blue-deep) 100%);
    box-shadow: 0 14px 34px rgba(0, 0, 0, 0.25);
    color: var(--ink-white);
  }
  .brand {
    position: absolute;
    left: 70px;
    top: 330px;
    display: flex;
    align-items: center;
    gap: 16px;
  }
  .brand-dot {
    width: 18px;
    height: 18px;
    border-radius: 50%;
    background: var(--ink-white);
  }
  .brand-name {
    font-family: "Marcellus", serif;
    font-size: 54px;
    letter-spacing: 0.5px;
    color: var(--ink-white);
  }
  .divider {
    position: absolute;
    left: 530px;
    top: 110px;
    width: 2px;
    height: 380px;
    background: var(--ink-white);
  }
  .divider::before {
    content: "";
    position: absolute;
    left: -2px;
    top: 0;
    width: 6px;
    height: 70px;
    background: var(--ink-white);
  }
  .details {
    position: absolute;
    left: 570px;
    top: 104px;
    width: 440px;
  }
  .person-name {
    font-family: "Cinzel", serif;
    font-weight: 600;
    font-size: 40px;
    letter-spacing: 2px;
    line-height: 1;
  }
  .person-title {
    font-family: "Cinzel", serif;
    font-size: 25px;
    letter-spacing: 1.5px;
    margin-top: 8px;
  }
  .address {
    font-family: "Marcellus", serif;
    font-size: 21px;
    line-height: 1.45;
    margin-top: 36px;
    color: var(--ink-soft);
  }
  .contact-list {
    list-style: none;
    margin-top: 16px;
    font-family: "Marcellus", serif;
    font-size: 20px;
    color: var(--ink-soft);
  }
  .contact-item {
    display: flex;
    align-items: center;
    gap: 14px;
    line-height: 1.55;
  }
  .contact-icon {
    width: 20px;
    height: 20px;
    flex: none;
  }
</style>
</head>
<body>
  <main class="card">
    <div class="brand">
      <span class="brand-dot"></span>
      <span class="brand-name">Voltaline Inc.</span>
    </div>

    <div class="divider"></div>

    <section class="details">
      <h1 class="person-name">Daniel Harlow</h1>
      <p class="person-title">CEO/Founder</p>

      <p class="address">4120 Cedar Hollow Road<br>Riverton, Missouri 63190</p>

      <ul class="contact-list">
        <li class="contact-item">
          <svg class="contact-icon" viewBox="0 0 20 20" aria-hidden="true"><path d="M5 2 L8 6 L6.5 8 Q8 12 12 13.5 L14 12 L18 15 L16 18 Q10 18 6 14 Q2 10 2 4 Z" fill="#fff"/></svg>
          <span>314 555 0172</span>
        </li>
        <li class="contact-item">
          <svg class="contact-icon" viewBox="0 0 20 20" aria-hidden="true"><rect x="5" y="1.5" width="10" height="17" rx="1.5" fill="none" stroke="#fff" stroke-width="1.8"/><circle cx="10" cy="15.5" r="1" fill="#fff"/></svg>
          <span>314 555 0248</span>
        </li>
        <li class="contact-item">
          <svg class="contact-icon" viewBox="0 0 20 20" aria-hidden="true"><rect x="2" y="8" width="16" height="9" rx="1" fill="#fff"/><rect x="5" y="2" width="10" height="7" fill="none" stroke="#fff" stroke-width="1.6"/></svg>
          <span>314 555 0391</span>
        </li>
        <li class="contact-item">
          <svg class="contact-icon" viewBox="0 0 20 20" aria-hidden="true"><rect x="2" y="4" width="16" height="12" rx="1" fill="#fff"/><path d="M2.5 4.5 L10 11 L17.5 4.5" fill="none" stroke="#1c5bb3" stroke-width="1.6"/></svg>
          <span>hello@voltalinepower.com</span>
        </li>
        <li class="contact-item">
          <svg class="contact-icon" viewBox="0 0 20 20" aria-hidden="true"><circle cx="10" cy="10" r="8" fill="none" stroke="#fff" stroke-width="1.6"/><ellipse cx="10" cy="10" rx="3.5" ry="8" fill="none" stroke="#fff" stroke-width="1.3"/><line x1="2" y1="10" x2="18" y2="10" stroke="#fff" stroke-width="1.3"/></svg>
          <span>www.voltalinepower.com</span>
        </li>
      </ul>
    </section>
  </main>
</body>
</html>
```